Tall Cedar Builders Business Card

I'm looking for a business card design for a start-up Handyman/Construction Company. The organization will double as a ministry to the homeless, hoping to create job opportunity and training to the homeless, providing a pathway back to being "homed". I'm looking for a simple to "seeming" simple design. Open to all thoughts.

Industry/Entity Type

Ministry

Requirements
Must have
• Logo (Attached), Name, Phone, Email and Address. Note - "*Registered and Insured".

```html
<!DOCTYPE html>
<html lang="en">
<head>
<meta charset="utf-8">
<title>Tall Cedar Builders Business Card</title>
<link rel="stylesheet" href="https://fonts.googleapis.com/css2?family=Open+Sans:wght@400;600;700&display=swap">
<style>
  :root {
    --backdrop: #2a2a2a;
    --card: #ffffff;
    --ink: #111111;
    --navy: #223a5e;
    --band: #000000;
    --muted: #444444;
  }
  html, body {
    margin: 0;
    width: 1200px;
    height: 902px;
    overflow: hidden;
    background: var(--backdrop);
    font-family: "Open Sans", Arial, sans-serif;
  }
  .card {
    position: absolute;
    left: 80px;
    top: 157px;
    width: 1040px;
    height: 587px;
    background: var(--card);
    overflow: hidden;
  }
  .brand-name {
    position: absolute;
    left: 58px;
    top: 52px;
    margin: 0;
    font-size: 40px;
    font-weight: 700;
    color: var(--navy);
    letter-spacing: 0.5px;
  }
  .holder {
    position: absolute;
    left: 150px;
    top: 238px;
    width: 220px;
    text-align: center;
  }
  .holder-name {
    margin: 0;
    font-size: 43px;
    font-weight: 400;
    color: var(--navy);
    text-decoration: underline;
    text-decoration-thickness: 2px;
    text-underline-offset: 6px;
    line-height: 1.2;
    white-space: nowrap;
  }
  .holder-title {
    margin: 8px 0 0;
    font-size: 17px;
    color: var(--muted);
  }
  .contact {
    position: absolute;
    right: 48px;
    top: 74px;
    text-align: right;
    font-size: 29px;
    line-height: 33px;
    color: var(--ink);
  }
  .contact p { margin: 0 0 22px; }
  .contact .web { margin-top: 30px; }
  .wave {
    position: absolute;
    left: 0;
    bottom: 0;
    width: 1040px;
    height: 587px;
  }
</style>
</head>
<body>
  <div class="card">
    <svg class="wave" viewBox="0 0 344 194" preserveAspectRatio="none" aria-hidden="true">
      <path d="M0 147 C70 138 150 118 200 120 C222 121 214 150 226 161 C244 174 300 170 344 166 L344 194 L0 194 Z" fill="var(--band)"/>
      <path d="M0 145 C70 136 150 116 200 118 C225 119 216 150 230 160 C250 172 300 168 344 164" fill="none" stroke="var(--navy)" stroke-width="2"/>
    </svg>

    <h1 class="brand-name">Tall Cedar Builders</h1>

    <div class="holder">
      <p class="holder-name">Your Name</p>
      <p class="holder-title">Founder &amp; CEO</p>
    </div>

    <div class="contact">
      <p>Telephone:<br>0123.456.789</p>
      <p>Address:<br>19xx street line,<br>City Name - Zipcode,<br>Country</p>
      <p>Email: name@mail.com</p>
      <p class="web">www.sitename.com</p>
    </div>
  </div>
</body>
</html>
```